orbit wellness loft
Project: logo for fitness studio
logo for fitness studio - Health
logo for fitness studio
Simple
Laura Whitfield
Certified Personal Trainer
482 W. Timber Ridge Rd. ElReno Ok. 73021
orbitwellness.owl@examplemail.test
I have already sent you most of my information .If you need more let me know .
Donna01 Donna01
I can't figure out how to change my brief. The email is wrong it's .owl@examplemail.test not .wol@examplemail.test so sorry. Also not so sure I like the black. The feeling I'm after is beach, sun and sand etc. thanks

```html
<!DOCTYPE html>
<html lang="en">
<head>
<meta charset="utf-8">
<title>orbit wellness loft — stationery</title>
<link href="https://fonts.googleapis.com/css2?family=Poppins:wght@300;400;600&display=swap" rel="stylesheet">
<style>
  :root{
    --teal:#1fb3ad;
    --teal-soft:#9fdcd8;
    --grey-dark:#5b5f63;
    --grey-light:#b9bcbe;
    --ink:#4a4f52;
    --ink-deep:#2e3b3b;
    --paper:#ffffff;
    --bg:#ffffff;
  }
  *{box-sizing:border-box;margin:0;padding:0}
  html,body{width:1200px;height:936px;overflow:hidden;background:var(--bg)}
  body{font-family:'Poppins',sans-serif;color:var(--ink);position:relative}
  .sheet{position:absolute;background:var(--paper);overflow:hidden;
    box-shadow:0 2px 10px rgba(0,0,0,.18)}
  .wave{position:absolute;left:0;bottom:0;display:block}

  .brand{display:flex;align-items:center;gap:8px;color:var(--teal);font-weight:300;white-space:nowrap}
  .brand-dot{border-radius:50%;background:var(--teal-soft);flex:none}

  /* letterhead */
  .letterhead{left:60px;top:30px;width:470px;height:650px}
  .letterhead .brand{position:absolute;left:30px;top:28px;font-size:15px}
  .letterhead .brand-dot{width:22px;height:22px}
  .letter{position:absolute;left:30px;top:84px;width:400px;font-size:7px;line-height:10px;color:#6b7073}
  .letter p{margin-bottom:9px}
  .signature{width:50px;height:16px;background:#e6e8e9;border-radius:3px;margin:4px 0 6px}
  .contacts{position:absolute;right:28px;bottom:104px;font-size:7px;line-height:12px;text-align:right;color:var(--ink);z-index:1}
  .contacts li{list-style:none;display:flex;justify-content:flex-end;align-items:center;gap:5px}
  .contacts svg{width:8px;height:8px;fill:var(--teal)}
  .address{position:absolute;left:30px;bottom:22px;font-size:7px;line-height:10px;color:#fff;z-index:1}

  /* folder */
  .folder{left:620px;top:26px;width:520px;height:676px}
  .folder .brand{position:absolute;left:0;right:0;top:250px;justify-content:center;font-size:34px;gap:14px}
  .folder .brand-dot{width:56px;height:56px}
  .folder .site{position:absolute;left:0;right:0;bottom:48px;text-align:center;font-size:13px;
    font-weight:600;letter-spacing:4px;color:var(--ink-deep)}

  /* business cards */
  .card{left:40px;width:200px;height:110px}
  .card-front{top:696px}
  .card-back{top:812px}
  .card-front .brand{position:absolute;left:12px;top:12px;font-size:8px;gap:4px}
  .card-front .brand-dot{width:12px;height:12px}
  .card-front .person{position:absolute;right:12px;top:12px;text-align:right}
  .person-name{font-size:9px;color:var(--teal)}
  .person-title{font-size:5.5px;color:#7a7f82}
  .card-back .brand{position:absolute;left:0;right:0;top:26px;justify-content:center;font-size:11px;gap:5px}
  .card-back .brand-dot{width:16px;height:16px}

  /* envelopes */
  .envelope-front{left:290px;top:740px;width:420px;height:170px}
  .envelope-front .brand{position:absolute;left:16px;top:14px;font-size:10px;gap:5px}
  .envelope-front .brand-dot{width:14px;height:14px}
  .envelope-front .return{position:absolute;left:16px;top:38px;font-size:6px;line-height:9px;color:#7a7f82}
  .envelope-back{left:730px;top:740px;width:440px;height:160px}
  .envelope-back .site{position:absolute;left:0;right:0;top:34px;text-align:center;font-size:12px;
    font-weight:600;letter-spacing:4px;color:var(--teal)}
</style>
</head>
<body>

<svg width="0" height="0" style="position:absolute" aria-hidden="true">
  <symbol id="wave" viewBox="0 0 200 60" preserveAspectRatio="none">
    <path d="M0 30 C60 50 120 12 200 0 L200 6 C120 18 60 54 0 36Z" fill="var(--grey-dark)"/>
    <path d="M0 36 C60 54 120 18 200 6 L200 12 C120 24 60 58 0 42Z" fill="var(--grey-light)"/>
    <path d="M0 44 C60 60 120 26 200 16 L200 60 L0 60Z" fill="var(--teal)"/>
  </symbol>
</svg>

<!-- Letterhead -->
<section class="sheet letterhead">
  <div class="brand"><span class="brand-dot"></span>orbit wellness loft</div>
  <div class="letter">
    <p>June 12, 2024</p>
    <p>Dear Sir,<br>Mr. Allen Reyes<br>ABC Building 4F, Studio Lane</p>
    <p>Thank you for your interest in our studio classes. We offer small group sessions, personal training and open floor hours through the week. Every plan begins with a short review of your goals so that each session fits your pace and schedule.</p>
    <p>Our trainers guide members through strength, mobility and recovery work in a calm space near the water. Please reply to this letter to book a first visit.</p>
    <p>We look forward to welcoming you and helping you feel your best all season long.</p>
    <p>Best Regards,</p>
    <div class="signature" role="img" aria-label="Handwritten signature"></div>
    <p>Laura Whitfield<br>Certified Personal Trainer</p>
  </div>
  <svg class="wave" width="470" height="130" viewBox="0 0 470 130">
    <path d="M0 20 C150 0 300 58 470 60 L470 68 C300 66 150 8 0 28Z" fill="var(--grey-dark)"/>
    <path d="M0 28 C150 8 300 66 470 68 L470 74 C300 72 150 14 0 34Z" fill="var(--grey-light)"/>
    <path d="M0 38 C150 18 300 76 470 78 L470 130 L0 130Z" fill="var(--teal)"/>
  </svg>
  <ul class="contacts">
    <li>580-555-0147 <svg viewBox="0 0 10 10"><path d="M2 1l2 0 1 2.5-1.2 1a6 6 0 002.7 2.7l1-1.2L10 7v2a1 1 0 01-1 1A9 9 0 011 2a1 1 0 011-1z"/></svg></li>
    <li>orbitwellness.owl@examplemail.test <svg viewBox="0 0 10 10"><path d="M0 2h10v6H0z"/></svg></li>
    <li>www.yourwebsitename.com <svg viewBox="0 0 10 10"><circle cx="5" cy="5" r="5"/></svg></li>
  </ul>
  <p class="address">482 W. Timber Ridge Rd.<br>ElReno Ok. 73021</p>
</section>

<!-- Presentation folder -->
<section class="sheet folder">
  <div class="brand"><span class="brand-dot"></span>orbit wellness loft</div>
  <svg class="wave" width="520" height="250"><use href="#wave"/></svg>
  <p class="site">www.yourwebsitename.com</p>
</section>

<!-- Business card front -->
<section class="sheet card card-front">
  <div class="brand"><span class="brand-dot"></span>orbit wellness loft</div>
  <div class="person">
    <p class="person-name">Laura Whitfield</p>
    <p class="person-title">Certified Personal Trainer</p>
  </div>
  <svg class="wave" width="200" height="52"><use href="#wave"/></svg>
</section>

<!-- Business card back -->
<section class="sheet card card-back">
  <div class="brand"><span class="brand-dot"></span>orbit wellness loft</div>
  <svg class="wave" width="200" height="46"><use href="#wave"/></svg>
</section>

<!-- Envelope front -->
<section class="sheet envelope-front">
  <div class="brand"><span class="brand-dot"></span>orbit wellness loft</div>
  <p class="return">482 W. Timber Ridge Rd.<br>ElReno Ok. 73021</p>
  <svg class="wave" width="420" height="80"><use href="#wave"/></svg>
</section>

<!-- Envelope back -->
<section class="sheet envelope-back">
  <p class="site">www.yourwebsitename.com</p>
  <svg class="wave" width="440" height="100" viewBox="0 0 440 100" preserveAspectRatio="none">
    <path d="M0 20 Q220 -10 440 20 L440 100 L0 100Z" fill="var(--teal)"/>
  </svg>
</section>

</body>
</html>
```